Covid-19 Mortgage Housing Market Coaching

I need a one page 8.5 x 11 printable infographic to describe the following:
Housing and Mortgage Market Coach
Through your Employer Home-ownership Benefit
The Coronavirus has resulted in an unprecedented Government coordination to reduce the spread of the virus, as such, has altered the way we live and work.
As each of us looks to the potential impact of the Coronavirus to our financial stability, it can be difficult to obtain trusted information to help make sound financial decisions.
As part of your employee home ownership program through your employer, you have access to this educational coaching on the below topics:
• What is happening in the stock market and why it is happening.
• Motivation behind Feds cutting rates and how that translates to the lending market.
• Discuss the future of interest rates.
• Discuss the future of the housing market. How will the spring and summer housing markets be effected?
• Everyone says to refinance now. Is that really in my best interest? Learn how to do a refinance analysis and determine if refinancing is right for you.
Having a better understanding of what is happening in the financial markets, with interest rates and the housing market can help you successfully navigate this rapidly evolving situation.
Please be sure that our phone number is prominently displayed 1-800-555-0182 and our web address www.lanternroofguild.com

```html
<!DOCTYPE html>
<html lang="en">
<head>
<meta charset="utf-8">
<title>Lantern Roof Guild – Housing and Mortgage Market Coaching</title>
<link rel="stylesheet" href="https://fonts.googleapis.com/css2?family=Source+Sans+3:wght@300;400;600&family=Roboto:wght@300;400;700&display=swap">
<style>
  :root {
    --bg: #b5d0e0;
    --ink: #1c2630;
    --navy: #1f3f68;
    --brand-green: #6aae48;
    --white: #ffffff;
    --ring: #d6e6ef;
    --icon-line: #9cc0d6;
    --icon-dark: #26343c;
    --rule: #eef5f9;
  }
  * { box-sizing: border-box; margin: 0; padding: 0; }
  html, body { width: 928px; height: 1200px; overflow: hidden; }
  body {
    background: var(--bg);
    font-family: "Source Sans 3", Arial, sans-serif;
    color: var(--ink);
  }
  .page { position: relative; width: 928px; height: 1200px; }

  .brand {
    position: absolute; left: 80px; top: 62px;
    display: flex; align-items: center; gap: 14px;
  }
  .brand-mark { width: 44px; height: 44px; background: var(--brand-green); }
  .brand-text { display: flex; flex-direction: column; }
  .brand-name {
    font-size: 32px; font-weight: 600; color: var(--navy); letter-spacing: -0.5px; line-height: 1;
  }
  .brand-tagline { font-size: 15px; color: var(--navy); margin-top: 4px; }

  .headline {
    position: absolute; left: 74px; top: 166px; width: 390px;
    font-size: 22.5px; font-weight: 600; line-height: 1.3; color: var(--ink);
  }

  .hero {
    position: absolute; left: 534px; top: 155px; width: 382px; height: 382px;
    border-radius: 50%; border: 3px solid var(--white);
    padding: 8px; background: var(--bg);
  }
  .hero-art {
    width: 100%; height: 100%; border-radius: 50%;
    background: radial-gradient(circle at 50% 40%, #f4c0ac 0%, #eaa58e 18%, #5b9bc3 40%, #ffffff 75%);
  }
  .virus-art {
    position: absolute; left: 466px; top: 136px; width: 150px; height: 150px;
    border-radius: 50%;
    background: radial-gradient(circle, #ee6a78 0%, #e24b5a 45%, rgba(226,75,90,0) 70%);
  }

  .blob {
    position: absolute; background: var(--white);
    box-shadow: 0 0 0 3px var(--bg), 0 0 0 5px var(--white);
  }
  .dot { position: absolute; background: var(--white); border-radius: 50%; }

  .blob-intro {
    left: 208px; top: 325px; width: 272px; height: 220px;
    border-radius: 46% 54% 48% 52% / 40% 50% 50% 60%;
  }
  .blob-intro p {
    position: absolute; left: 10px; right: 10px; top: 90px;
    font-family: "Roboto", Arial, sans-serif; font-weight: 300;
    font-size: 18px; line-height: 24px; text-align: center;
  }
  .blob-intro svg { position: absolute; left: 34px; top: 28px; }

  .blob-card {
    font-size: 14.5px; line-height: 18px;
  }
  .blob-card p { position: absolute; white-space: nowrap; }
  .blob-card p span { display: block; }
  .blob-card svg { position: absolute; }

  .blob-advisor {
    left: 50px; top: 545px; width: 284px; height: 212px;
    border-radius: 40% 55% 48% 45% / 45% 42% 58% 55%;
  }
  .blob-advisor p { top: 70px; left: 0; }
  .blob-advisor svg { left: 76px; top: 10px; }

  .blob-impact {
    left: 352px; top: 572px; width: 252px; height: 178px;
    border-radius: 50% 48% 52% 44% / 42% 48% 52% 58%;
  }
  .blob-impact p { top: 54px; left: 0; right: 0; text-align: center; }
  .blob-impact svg { left: 118px; top: -6px; }

  .blob-coaching {
    left: 636px; top: 556px; width: 232px; height: 202px;
    border-radius: 44% 56% 52% 48% / 50% 45% 55% 50%;
  }
  .blob-coaching p { top: 82px; left: 10px; }
  .blob-coaching svg { left: 36px; top: 14px; }

  .rule { position: absolute; left: 65px; width: 805px; height: 1px; background: var(--rule); }

  .topic {
    position: absolute; display: flex; align-items: flex-start; gap: 10px;
  }
  .topic-icon {
    flex: none; width: 84px; height: 84px; border-radius: 50%;
    background: var(--white); border: 3px solid var(--ring);
    box-shadow: 0 0 0 2px var(--white);
    display: flex; align-items: center; justify-content: center;
  }
  .topic p {
    font-size: 15px; font-weight: 600; line-height: 18.5px; padding-top: 12px; white-space: nowrap;
  }

  .summary {
    position: absolute; left: 65px; top: 1070px; width: 810px;
    font-family: "Roboto", Arial, sans-serif; font-weight: 700;
    font-size: 18.5px; line-height: 23px; color: var(--ink);
  }

  .contact {
    position: absolute; top: 1153px; left: 0; width: 928px;
    display: flex; justify-content: center; gap: 72px;
    font-family: "Roboto", Arial, sans-serif; font-size: 20.5px; color: var(--ink);
  }
  .contact span { display: flex; align-items: center; gap: 6px; }
</style>
</head>
<body>
<main class="page">

  <header class="brand">
    <div class="brand-mark"></div>
    <div class="brand-text">
      <span class="brand-name">Lantern Roof Guild</span>
      <span class="brand-tagline">Employee Home Ownership Program</span>
    </div>
  </header>

  <h1 class="headline">Does Covid-19 Have you Concerned about the Real Estate Market, Interest Rates and Mortgage Loans?</h1>

  <div class="virus-art" role="img" aria-label="Red coronavirus particles floating in the air"></div>
  <div class="hero">
    <div class="hero-art" role="img" aria-label="Illustration of a man in a face mask and orange scarf coughing into his hand"></div>
  </div>

  <section class="blob blob-intro">
    <svg width="90" height="56" viewBox="0 0 90 56" fill="none" stroke="var(--icon-line)" stroke-width="2.5">
      <rect x="6" y="2" width="56" height="28" rx="2"/>
      <circle cx="34" cy="16" r="8"/>
      <path d="M2 46 h10 l14 -8 h18 M12 54 h24 l18 -12"/>
      <path d="M52 30 l16 -14 l16 14 M56 28 v26 h24 v-26 M64 54 v-12 h8 v12"/>
    </svg>
    <p>Home ownership options, advise, coaching and money saving opportunities for employees.</p>
  </section>
  <div class="dot" style="left:362px;top:308px;width:62px;height:52px;"></div>
  <div class="dot" style="left:432px;top:352px;width:24px;height:22px;"></div>

  <section class="blob blob-card blob-advisor">
    <svg width="68" height="56" viewBox="0 0 68 56" fill="none" stroke="var(--icon-line)" stroke-width="2">
      <path d="M28 2 l2 8 M38 0 v10 M48 2 l-2 8"/>
      <rect x="24" y="16" width="32" height="16" rx="2"/>
      <circle cx="40" cy="24" r="5"/>
      <rect x="2" y="34" width="8" height="20"/>
      <path d="M10 38 h14 l10 4 h-12 M10 52 h24 l30 -18"/>
    </svg>
    <p>
      <span style="margin-left:27px">As part of your employee benefits, you</span>
      <span style="margin-left:21px">have exclusive access to your own home</span>
      <span style="margin-left:17px">ownership benefits advisor who can</span>
      <span style="margin-left:15px">provide you information on the below as</span>
      <span style="margin-left:15px">well as money saving opportunities</span>
      <span style="margin-left:18px">related to refinancing, buying or</span>
      <span style="margin-left:23px">selling a home.</span>
    </p>
  </section>
  <div class="dot" style="left:262px;top:555px;width:22px;height:20px;"></div>
  <div class="dot" style="left:196px;top:742px;width:26px;height:24px;"></div>

  <section class="blob blob-card blob-impact">
    <svg width="60" height="54" viewBox="0 0 60 54" fill="none" stroke="var(--icon-line)" stroke-width="2">
      <path d="M2 4 q22 6 44 18 M40 16 l8 8 l-10 2"/>
      <rect x="2" y="30" width="8" height="22"/>
      <rect x="16" y="36" width="8" height="16"/>
      <rect x="30" y="42" width="8" height="10"/>
      <circle cx="50" cy="45" r="7" fill="var(--icon-line)"/>
    </svg>
    <p>
      <span>As each of us looks to the potential</span>
      <span>impact of the Coronavirus to our</span>
      <span>financial stability, it can be difficult</span>
      <span>to obtain trusted information to</span>
      <span>help make sound financial</span>
      <span>decisions.</span>
    </p>
  </section>
  <div class="dot" style="left:412px;top:570px;width:22px;height:20px;"></div>
  <div class="dot" style="left:550px;top:552px;width:50px;height:48px;"></div>

  <section class="blob blob-card blob-coaching">
    <svg width="74" height="62" viewBox="0 0 74 62" fill="none" stroke="var(--icon-line)" stroke-width="2">
      <rect x="2" y="4" width="40" height="26"/>
      <rect x="12" y="13" width="20" height="8" fill="var(--icon-line)" stroke="none"/>
      <circle cx="60" cy="6" r="5"/>
      <path d="M54 14 h12 v22 M54 14 v22 M58 36 v24 M62 36 v24"/>
      <circle cx="6" cy="44" r="4"/><circle cx="20" cy="44" r="4"/><circle cx="34" cy="44" r="4"/>
      <path d="M0 58 v-6 h12 v6 M14 58 v-6 h12 v6 M28 58 v-6 h12 v6"/>
    </svg>
    <p>
      <span style="margin-left:20px">As part of your employee home</span>
      <span style="margin-left:6px">ownership program through</span>
      <span>your employer, you have access</span>
      <span>to this educational coaching</span>
      <span style="margin-left:10px">on the below topics:</span>
    </p>
  </section>
  <div class="dot" style="left:780px;top:748px;width:22px;height:20px;"></div>

  <div class="rule" style="top:796px;"></div>

  <section class="topic" style="left:71px;top:835px;">
    <div class="topic-icon">
      <svg width="50" height="50" viewBox="0 0 50 50" fill="var(--icon-dark)">
        <path d="M4 8 l20 20 l8 -8 l12 12" stroke="var(--icon-dark)" stroke-width="4" fill="none"/>
        <path d="M46 26 v12 h-12 z"/>
        <rect x="4" y="22" width="6" height="26"/><rect x="13" y="28" width="6" height="20"/>
        <rect x="22" y="34" width="6" height="14"/><rect x="31" y="32" width="6" height="16"/><rect x="40" y="40" width="6" height="8"/>
      </svg>
    </div>
    <p>What is happening in<br>the interest rate<br>market and why is it<br>happening.</p>
  </section>

  <section class="topic" style="left:333px;top:835px;">
    <div class="topic-icon">
      <svg width="50" height="50" viewBox="0 0 50 50" fill="var(--icon-dark)">
        <path d="M20 2 h10 v12 h6 l-11 12 l-11 -12 h6 z"/>
        <path d="M6 12 v14 M44 12 v14 M11 18 v6 M39 18 v6" stroke="var(--icon-dark)" stroke-width="2"/>
        <ellipse cx="25" cy="32" rx="10" ry="4"/><ellipse cx="14" cy="40" rx="10" ry="4"/>
        <ellipse cx="36" cy="40" rx="10" ry="4"/><ellipse cx="25" cy="46" rx="10" ry="3.5"/>
      </svg>
    </div>
    <p>Motivation behind Feds<br>cutting rates and how that<br>translates to the lending<br>market.</p>
  </section>

  <section class="topic" style="left:618px;top:835px;">
    <div class="topic-icon">
      <svg width="50" height="54" viewBox="0 0 50 54" fill="var(--icon-dark)">
        <rect x="8" y="4" width="34" height="46" rx="3"/>
        <rect x="12" y="8" width="22" height="10" fill="var(--white)"/>
        <g fill="var(--white)">
          <rect x="12" y="22" width="6" height="6"/><rect x="21" y="22" width="6" height="6"/><rect x="30" y="22" width="6" height="6"/>
          <rect x="21" y="31" width="6" height="6"/><rect x="30" y="31" width="6" height="15"/><rect x="21" y="40" width="6" height="6"/>
        </g>
        <circle cx="40" cy="10" r="8" stroke="var(--white)" stroke-width="2"/>
        <circle cx="10" cy="44" r="8" stroke="var(--white)" stroke-width="2"/>
      </svg>
    </div>
    <p style="padding-top:6px">Discuss the future of<br>interest rates.</p>
  </section>

  <section class="topic" style="left:168px;top:955px;">
    <div class="topic-icon">
      <svg width="54" height="50" viewBox="0 0 54 50" fill="var(--icon-dark)">
        <path d="M16 16 l14 -12 l14 12 v18 h-28 z"/>
        <text x="30" y="30" font-family="Roboto, sans-serif" font-size="16" font-weight="700" fill="var(--white)" text-anchor="middle">$</text>
        <rect x="2" y="34" width="7" height="14"/>
        <path d="M9 36 h14 l8 4 h-10 M9 46 h22 l20 -12 l-4 -2 l-14 6"/>
      </svg>
    </div>
    <p style="padding-top:16px">Discuss the future of the<br>housing market. How will the<br>spring and summer housing<br>markets be effected?</p>
  </section>

  <section class="topic" style="left:464px;top:955px;">
    <div class="topic-icon">
      <svg width="50" height="50" viewBox="0 0 50 50" fill="none" stroke="var(--icon-dark)" stroke-width="6">
        <path d="M8 22 a17 17 0 0 1 30 -10"/>
        <path d="M42 28 a17 17 0 0 1 -30 10"/>
        <path d="M34 4 l8 10 l-12 2 z M16 46 l-8 -10 l12 -2 z" fill="var(--icon-dark)" stroke-width="1"/>
        <text x="25" y="32" font-family="Roboto, sans-serif" font-size="18" font-weight="700" fill="var(--icon-dark)" stroke="none" text-anchor="middle">$</text>
      </svg>
    </div>
    <p style="padding-top:10px">Everyone says to refinance now. Is that<br>really in my best interest? Learn how<br>to do a refinance analysis and deter-<br>mine if refinancing is right for you.</p>
  </section>

  <p class="summary">Having a better understanding of what is happening in the financial markets, with interest rates and the housing market can help you successfully navigate this rapidly evolving situation.</p>

  <div class="rule" style="top:1144px;"></div>

  <footer class="contact">
    <span>
      <svg width="20" height="20" viewBox="0 0 20 20"><circle cx="10" cy="10" r="10" fill="var(--icon-dark)"/><path d="M6 5 l2 -1 l2 3 l-1.5 1.5 q1 2.5 3 3.5 l1.5 -1.5 l3 2 l-1 2 q-5 1 -9 -9" fill="var(--white)"/></svg>
      1-800-555-0182
    </span>
    <span>
      <svg width="20" height="20" viewBox="0 0 20 20" fill="none" stroke="var(--white)" stroke-width="1.3"><circle cx="10" cy="10" r="10" fill="var(--icon-dark)" stroke="none"/><circle cx="10" cy="10" r="6"/><path d="M4 10 h12 M10 4 q-4 6 0 12 q4 -6 0 -12"/></svg>
      www.lanternroofguild.com
    </span>
  </footer>

</main>
</body>
</html>
```